Need a cover for eBook:
Title is: 47 Blunders That Sink Your Indie-Released eBook.
Remarks about the title: I know that is difficult to design a cover with a number. You can add the word TOP (in caps or not) before 47 blunders. It is not mandatory to insert the word TOP. It is up to you if you think you can create a better cover.
Subtitle is: A Newcomer's Manual for Releasing Solo, Shaping Pictures and Words, Arranging Pages, Boosting Sign-ups and Moving More Copies
Author: Dennis R. Albrook
Publisher: Lanternfield Works
The book made the presentation of errors that can occur during the production of an ebook. Title must be big, the title should be readable even when the image is reduced in size. No photo please.
I join my projects as an example. Do what you want but I need impact.

Target Market(s)

Book to sell first at Brisco Leafreader Shop. Target is authors, men or women, who want to produce ebooks.

Industry/Entity Type

Publishing Company

Font styles to use
Sans Serif

Colors
3176b5
9bcb3c

Requirements
Must have
• High readability when cover is small.
• Here is the definition of the word KILL
• put an end to or cause the failure or defeat of (something).
• "the committee voted to kill the project"
• synonyms: destroy, put an end to, end, extinguish, dash, quash, ruin, wreck, shatter, smash, crush, scotch, thwart; informalput the kibosh on, stymie, scuttle
• "this would kill all hopes of progress"
• veto, defeat, vote down, rule against, reject, throw out, overrule, overturn, put a stop to, quash, squash
• "an opposition attempt to kill the bill"
Nice to have
• I suggested 2 colors but you can you use another one or two. I want cover that sell. There is so bright ideas here. Come on down!
Should not have
• No picture or photo. If a photo or an object had power to the cover, you can insert one. I don't want a photo-collage.

```html
<!DOCTYPE html>
<html lang="en">
<head>
<meta charset="utf-8">
<title>47 Blunders That Sink Your Indie-Released eBook — Dennis R. Albrook</title>
<link rel="stylesheet" href="https://fonts.googleapis.com/css2?family=Anton&family=Oswald:wght@600&display=swap">
<style>
  :root {
    --cover-blue-light: #3f8fd6;
    --cover-blue: #3176b5;
    --cover-blue-deep: #123f72;
    --title-green: #9bcb3c;
    --author-navy: #0e2b4f;
    --subtitle-white: #ffffff;
    --metal-light: #d9dde0;
    --metal-dark: #7c8389;
  }
  html, body {
    margin: 0;
    padding: 0;
    width: 800px;
    height: 1200px;
    overflow: hidden;
    background: var(--cover-blue-deep);
  }
  .book-cover {
    position: relative;
    width: 800px;
    height: 1200px;
    overflow: hidden;
    background:
      radial-gradient(ellipse 70% 55% at 50% 30%, var(--cover-blue-light) 0%, var(--cover-blue) 55%, transparent 100%),
      linear-gradient(180deg, var(--cover-blue) 0%, var(--cover-blue) 45%, var(--cover-blue-deep) 100%);
  }
  .cover-type {
    position: absolute;
    inset: 0;
    width: 800px;
    height: 1200px;
  }
  .author-name {
    font-family: "Anton", sans-serif;
    fill: var(--author-navy);
  }
  .title-line {
    font-family: "Anton", sans-serif;
    fill: var(--title-green);
  }
  .subtitle-line {
    font-family: "Oswald", sans-serif;
    font-weight: 600;
    fill: var(--subtitle-white);
  }
  .hero-object {
    position: absolute;
    left: 327px;
    top: 447px;
    width: 180px;
    height: 220px;
    border-radius: 14px 14px 22px 22px;
    background: linear-gradient(90deg, var(--metal-dark) 0%, var(--metal-light) 45%, var(--metal-dark) 100%);
    transform: rotate(-8deg);
  }
</style>
</head>
<body>
  <main class="book-cover">
    <div class="hero-object" role="img" aria-label="A dented galvanised metal trash can tilting over, symbolising a discarded ebook"></div>
    <svg class="cover-type" viewBox="0 0 800 1200" aria-labelledby="cover-title">
      <title id="cover-title">47 Blunders That Sink Your Indie-Released eBook</title>
      <text class="author-name" x="170" y="84" font-size="46" textLength="460" lengthAdjust="spacingAndGlyphs">DENNIS R. ALBROOK</text>

      <text class="title-line title-number" x="53" y="307" font-size="176" textLength="693" lengthAdjust="spacingAndGlyphs">47 BLUNDERS</text>
      <text class="title-line title-bridge" x="120" y="424" font-size="102" textLength="560" lengthAdjust="spacingAndGlyphs">THAT SINK YOUR</text>
      <text class="title-line title-qualifier" x="113" y="753" font-size="96" textLength="573" lengthAdjust="spacingAndGlyphs">INDIE-RELEASED</text>
      <text class="title-line title-format" x="143" y="949" font-size="212" textLength="513" lengthAdjust="spacingAndGlyphs">EBOOK</text>

      <text class="subtitle-line" x="87" y="1009" font-size="29" textLength="627" lengthAdjust="spacingAndGlyphs">A NEWCOMER'S MANUAL FOR RELEASING SOLO,</text>
      <text class="subtitle-line" x="87" y="1048" font-size="29" textLength="627" lengthAdjust="spacingAndGlyphs">SHAPING PICTURES AND WORDS, ARRANGING PAGES,</text>
      <text class="subtitle-line" x="87" y="1087" font-size="29" textLength="627" lengthAdjust="spacingAndGlyphs">BOOSTING SIGN-UPS AND MOVING MORE COPIES</text>
    </svg>
  </main>
</body>
</html>
```